FUN Construction Open House Invitation

Open House for New Office of MVDP Construction, we have a logo, not sure what other graphics to put on the invitation and make it fun

Main target audience: Residential Building Architects (Custom Homes)
so we want to maybe target it towards that with a sketch of design/house/plans?
Drinks and food at: Verdel Cantina around the corner
LUCKY DOOR PRIZES: zentab, etc (need to be present to win)
Current BORING design attached
Event is on Thursday, 7/15 from 3-6 pm
Location: 718 Elmcrest, Suite 502-7 in Laguna Beach
Company: MVDP Construction (logo attached)
RSVP by 7/12 to office@mvdpbuild.example or 949-555-0172

Target Market(s)

Residential Building Architects for Custom Homes

Font styles to use
Other font styles liked:
• SOMETHING MODERN

Requirements
Must have
• Graphics, MODERN & FUN & ARTSY look but not too crowded
Should it be a charicature of the team? (with our english bulldog?)
A charicature of our english bulldog on a surfboard or skateboard or too cheesy?
Should not have
• Hammer or any other graphics like that, we are not a handyman company
High end custom home construction working with architects

```html
<!DOCTYPE html>
<html lang="en">
<head>
<meta charset="utf-8">
<title>MVDP Construction Open House Invitation</title>
<link rel="stylesheet" href="https://fonts.googleapis.com/css2?family=Krona+One&family=Catamaran:wght@400;500;700;800&display=swap">
<style>
  :root {
    --page-bg: #e4e4e4;
    --frame: #7c7c7c;
    --paper: #f6f6f6;
    --ink: #2a2a2a;
    --accent: #e5711a;
    --icon-fill: #f3d6bf;
  }
  * { margin: 0; padding: 0; box-sizing: border-box; }
  html, body { width: 989px; height: 1200px; overflow: hidden; background: var(--page-bg); }
  body { position: relative; font-family: "Catamaran", sans-serif; color: var(--ink); }

  .invite {
    position: absolute; left: 20px; top: 270px;
    width: 949px; height: 660px;
    background: var(--frame); padding: 18px;
  }
  .invite__paper { position: relative; width: 100%; height: 100%; background: var(--paper); overflow: hidden; }
  .abs { position: absolute; white-space: nowrap; line-height: 1.2; }

  .headline {
    left: 0; right: 0; top: 40px; text-align: center;
    font-family: "Krona One", sans-serif; font-size: 24px; letter-spacing: -0.3px; color: var(--ink);
  }
  .subhead {
    left: 0; right: 0; top: 90px; text-align: center;
    font-family: "Krona One", sans-serif; font-size: 26px; color: var(--accent);
  }

  .date-day { left: 58px; top: 186px; font-size: 40px; font-weight: 800; letter-spacing: 0.5px; }
  .date-divider { top: 168px; height: 104px; border-left: 3px dotted var(--accent); }
  .date-divider--a { left: 340px; }
  .date-divider--b { left: 600px; }
  .date-day-month { left: 343px; width: 257px; top: 162px; text-align: center; font-size: 40px; font-weight: 800; line-height: 54px; }
  .date-day-month sup { font-size: 22px; line-height: 0; vertical-align: 16px; }
  .date-time { left: 632px; top: 182px; font-size: 42px; font-weight: 700; }

  .venue-label { left: 0; right: 0; top: 282px; text-align: center; color: var(--accent); font-size: 28px; font-weight: 800; }
  .venue-address { left: 0; right: 0; top: 320px; text-align: center; font-size: 28px; font-weight: 500; }

  .perk-icon { width: 56px; height: 56px; border-radius: 8px; background: var(--icon-fill); }
  .perk-icon--food { left: 48px; top: 408px; }
  .perk-icon--prize { left: 480px; top: 406px; }
  .perk-title { color: var(--accent); font-weight: 800; font-size: 22px; }
  .perk-title span { color: var(--ink); font-weight: 500; }
  .perk-text { font-size: 22px; font-weight: 500; }
  .perk-food-title { left: 118px; top: 404px; }
  .perk-food-text { left: 118px; top: 434px; }
  .perk-divider { left: 455px; top: 402px; height: 68px; border-left: 3px dotted var(--accent); }
  .perk-prize-title { left: 552px; top: 402px; }
  .perk-prize-text { left: 552px; top: 432px; }

  .rsvp-title { left: 46px; top: 504px; font-size: 23px; font-weight: 800; }
  .rsvp-line { left: 46px; font-size: 23px; font-weight: 500; display: flex; align-items: center; gap: 8px; }
  .rsvp-line--email { top: 535px; }
  .rsvp-line--phone { top: 566px; }
  .rsvp-line .or { color: var(--accent); font-weight: 800; }
  .rsvp-line svg { width: 18px; height: 18px; flex: none; }
  .rsvp-line .web { margin-left: 10px; display: inline-flex; gap: 8px; align-items: center; }

  .brand { right: 40px; top: 548px; display: flex; align-items: center; gap: 10px; }
  .brand__mark { width: 20px; height: 20px; background: var(--accent); }
  .brand__name { font-size: 26px; font-weight: 800; color: var(--accent); text-transform: uppercase; letter-spacing: 1px; }
</style>
</head>
<body>
  <article class="invite">
    <div class="invite__paper">
      <h1 class="abs headline">RESIDENTIAL BUILDING ARCHITECTS</h1>
      <h2 class="abs subhead">(CUSTOM HOMES)</h2>

      <p class="abs date-day">THURSDAY</p>
      <div class="abs date-divider date-divider--a"></div>
      <p class="abs date-day-month">JULY 15<sup>TH</sup><br>2021</p>
      <div class="abs date-divider date-divider--b"></div>
      <p class="abs date-time">3 pm - 6 pm</p>

      <p class="abs venue-label">MVDP’s new office Location at</p>
      <p class="abs venue-address">718 Elmcrest, Suite 502-7 in Laguna Beach</p>

      <div class="abs perk-icon perk-icon--food" role="img" aria-label="Line icon of a burger and a drink cup"></div>
      <p class="abs perk-title perk-food-title">DRINKS AND FOOD AT:</p>
      <p class="abs perk-text perk-food-text">Verdel Cantina around the corner</p>
      <div class="abs perk-divider"></div>
      <div class="abs perk-icon perk-icon--prize" role="img" aria-label="Line icon of a hand holding a prize ticket"></div>
      <p class="abs perk-title perk-prize-title">LUCKY DOOR PRIZES: <span>zentab, etc</span></p>
      <p class="abs perk-text perk-prize-text">(need to be present to win)</p>

      <p class="abs rsvp-title">RSVP by 7/12 to</p>
      <p class="abs rsvp-line rsvp-line--email">
        <svg viewBox="0 0 18 18" aria-hidden="true"><rect x="1" y="4" width="16" height="11" rx="1.5" fill="var(--accent)"/><path d="M2 5l7 5 7-5" stroke="#fff" stroke-width="1.6" fill="none"/></svg>
        office@mvdpbuild.example <span class="or">or</span>
      </p>
      <p class="abs rsvp-line rsvp-line--phone">
        <svg viewBox="0 0 18 18" aria-hidden="true"><path d="M4 2l3 3-1.5 2a9 9 0 0 0 5.5 5.5L13 11l3 3-2 2.5C8 16 2 10 1.5 4z" fill="var(--accent)"/></svg>
        949-555-0172
        <span class="web">
          <svg viewBox="0 0 18 18" aria-hidden="true"><circle cx="9" cy="9" r="7.5" fill="none" stroke="var(--accent)" stroke-width="1.6"/><ellipse cx="9" cy="9" rx="3.2" ry="7.5" fill="none" stroke="var(--accent)" stroke-width="1.4"/><path d="M1.5 9h15" stroke="var(--accent)" stroke-width="1.4"/></svg>
          www.mvdpbuild.example
        </span>
      </p>

      <div class="abs brand">
        <span class="brand__mark"></span>
        <span class="brand__name">MVDP Construction</span>
      </div>
    </div>
  </article>
</body>
</html>
```